Educational clinic needs a new webpage design

I have a relatively new website but I am unhappy with the design. I was hoping the look of it would more match my logo, brochures, business cards, and postcards. The content is good and it's already mobile ready. The designer used square space, which I would like to keep if possible. My website is www.harborlightstudyhouse.example

Target Market(s)

Parents of school age children

Industry/Entity Type

Education

Number of Pages Required

5+ page

Requirements
Must have
• Pictures must depict the diversity of our students. We service all ages, from preschool through college and our students come from varying races.
Should not have
• I try to avoid the word "tutoring" because what we do is so much more. I like the tag line of "results that go beyond traditional tutoring"

```html
<!DOCTYPE html>
<html lang="en">
<head>
<meta charset="utf-8">
<title>Harbor Light Study House</title>
<link rel="stylesheet" href="https://fonts.googleapis.com/css2?family=Montserrat:wght@400;600;700&family=Open+Sans:wght@400;600&display=swap">
<style>
:root{
  --purple:#6b2a8c;
  --purple-deep:#4e1d69;
  --purple-soft:#8a4bb0;
  --green:#8cc63f;
  --green-pale:#dff0c4;
  --ink:#333;
  --grey:#666;
  --sky:#7fb6e6;
  --white:#fff;
}
*{box-sizing:border-box;margin:0;padding:0}
html,body{width:1200px;height:3651px;overflow:hidden}
body{position:relative;font-family:"Open Sans",Arial,sans-serif;color:var(--ink);background:var(--white)}
.section{position:absolute;left:0;width:1200px;overflow:hidden}
.abs{position:absolute}
.center{text-align:center}
.display{font-family:"Montserrat",Arial,sans-serif}

/* header */
.topbar{top:0;height:54px;background:var(--purple);z-index:3;color:var(--white);font-size:14px;font-family:"Montserrat",sans-serif}
.topbar .follow{left:80px;top:17px;display:flex;align-items:center;gap:14px}
.dot-icon{width:14px;height:14px;border-radius:50%;background:rgba(255,255,255,.75)}
.topbar .call{right:80px;top:17px;display:flex;align-items:center;gap:10px}
.brand{position:absolute;left:433px;top:0;width:331px;height:92px;background:var(--white);border:4px solid var(--purple);border-top:0;z-index:4;display:flex;align-items:center;justify-content:center;gap:12px}
.brand-mark{width:44px;height:44px;border-radius:50%;background:var(--purple)}
.brand-name{font-family:"Montserrat",sans-serif;font-weight:700;font-size:21px;color:var(--purple);line-height:1.1}
.nav{top:104px;left:0;width:1200px;z-index:3;display:flex;justify-content:center;font-family:"Montserrat",sans-serif;font-size:16px;color:var(--white)}
.nav a{color:inherit;text-decoration:none;padding:0 28px;border-left:1px solid rgba(255,255,255,.6);line-height:18px}
.nav a:first-child{border-left:0;color:var(--purple);font-weight:600}

/* hero */
.hero{top:0;height:677px;background:linear-gradient(180deg,#6fa9e0 0%,#a9d0f2 60%,#e6f1fb 100%)}
.hero-photo{left:230px;top:150px;width:760px;height:527px;background:linear-gradient(180deg,#c9a88a 0%,#6f8fb8 55%,#3b4f7a 100%);opacity:.55;border-radius:120px 120px 0 0}
.hero-title{top:340px;left:0;width:1200px;font-family:"Montserrat",sans-serif;font-size:58px;line-height:64px;color:var(--white);letter-spacing:1px;text-shadow:0 2px 6px rgba(0,0,0,.25)}
.slider-dots{top:622px;left:570px;display:flex;gap:10px}
.slider-dots span{width:12px;height:12px;border-radius:50%;background:rgba(255,255,255,.5)}
.slider-dots span:first-child{background:var(--white)}

/* programs */
.programs{top:677px;height:552px;background:#f7f7f7}
.program{width:320px;text-align:center}
.program h3{font-family:"Montserrat",sans-serif;font-weight:400;font-size:20px;color:var(--purple);margin-bottom:6px}
.program p{font-size:15px;line-height:21px;color:var(--ink)}
.hub{left:505px;top:177px;width:190px;height:190px;border-radius:50%;background:radial-gradient(circle,#8d5bb0 0%,#c2e08e 100%)}

/* quote */
.quote{top:1229px;height:365px;background:linear-gradient(120deg,#5c2478 0%,#8e55b3 55%,#6b2a8c 100%)}
.quote-mark{top:40px;left:0;width:1200px;font-family:"Montserrat",sans-serif;font-size:72px;line-height:60px;color:var(--green)}
.quote-text{top:100px;left:0;width:1200px;font-family:"Montserrat",sans-serif;font-size:26px;line-height:33px;color:var(--white)}
.quote-by{top:180px;left:0;width:1200px;font-size:17px;color:var(--white);font-weight:600}
.socials{top:231px;left:450px;display:flex;gap:12px}
.socials span{width:48px;height:48px;border:1px solid rgba(255,255,255,.55);background:rgba(255,255,255,.12)}
.socials span:first-child{background:var(--white)}
.socials-caption{top:300px;left:0;width:1200px;font-size:17px;color:var(--white)}

/* why choose */
.why{top:1594px;height:480px;background:var(--white)}
.why h2{left:80px;top:52px;font-family:"Montserrat",sans-serif;font-weight:400;font-size:42px;color:var(--purple)}
.why h2 b{font-weight:700}
.why .intro{left:80px;top:118px;width:640px;font-size:16px;line-height:22px;color:var(--ink)}
.checks{left:80px;top:176px;width:600px;list-style:none}
.checks li{position:relative;padding-left:34px;font-size:16px;line-height:22px;color:var(--grey);margin-bottom:18px}
.checks li svg{position:absolute;left:0;top:2px}
.price{left:80px;top:364px;display:flex;align-items:center;gap:24px}
.price strong{font-family:"Montserrat",sans-serif;font-size:54px;color:var(--purple);font-weight:700}
.price span{font-family:"Montserrat",sans-serif;font-size:20px;line-height:24px;color:var(--ink)}
.why-photo{left:730px;top:18px;width:340px;height:435px;background:linear-gradient(180deg,#f2e6d9 0%,#f0f3c0 55%,#f4c9d8 100%);border-radius:40px}

/* tutors */
.tutors{top:2074px;height:523px;background:linear-gradient(180deg,#5a2277 0%,#7d3fa6 50%,#9a6cc0 100%)}
.tutors h2,.clients h2,.contact h2{left:0;width:1200px;font-family:"Montserrat",sans-serif;font-weight:400;font-size:42px;text-align:center}
.tutors h2{top:50px;color:var(--white)}
.tutors h2 b,.contact h2 b{font-weight:700}
.card{top:122px;width:249px;height:335px;background:var(--white);text-align:center}
.card .photo{height:250px;background:linear-gradient(180deg,#dcdfe6 0%,#b8bfcc 100%)}
.card.open .photo{height:177px}
.card h3{font-family:"Montserrat",sans-serif;font-weight:400;font-size:20px;color:#222;margin-top:18px;letter-spacing:.5px}
.card .role{font-size:14px;color:var(--purple);margin-top:4px}
.card .bio{font-size:14px;line-height:19px;color:var(--grey);margin:4px 22px 0}
.card .links{display:flex;justify-content:center;gap:8px;margin-top:8px}
.card .links span{width:28px;height:28px;border-radius:50%;background:var(--purple-soft)}

/* clients */
.clients{top:2597px;height:519px;background:#f9f9f9}
.clients h2{top:52px;color:var(--purple)}
.clients h2 b{font-weight:700}
.clients .intro{top:116px;left:250px;width:700px;font-size:15px;line-height:22px;color:var(--ink);text-align:center}
.avatar{top:178px;width:97px;height:97px;border-radius:50%;background:linear-gradient(180deg,#e7d2bd,#8f7a6b)}
.client-name{top:295px;width:330px;font-family:"Montserrat",sans-serif;font-size:20px;color:#333;text-align:center}
.review{top:341px;width:328px;height:129px;background:var(--white);border:1px solid #ddd;padding:18px 22px;font-size:15px;line-height:22px;color:var(--ink);text-align:center}

/* contact */
.contact{top:3116px;height:467px;background:linear-gradient(120deg,#5c2478 0%,#8a4fb0 50%,#6b2a8c 100%)}
.contact h2{top:48px;color:var(--white)}
.label{font-family:"Montserrat",sans-serif;font-weight:600;font-size:16px;color:var(--white)}
.field{height:39px;border:1px solid rgba(255,255,255,.5);background:var(--purple-deep);color:var(--white);font-size:14px;padding:10px 12px}
.send{left:641px;top:332px;width:80px;height:80px;border-radius:50%;background:var(--purple-deep);border:4px solid var(--purple-soft);display:flex;align-items:center;justify-content:center}
.info{left:888px;width:200px;text-align:center;color:var(--white);font-size:14px}

/* footer */
.footer{top:3583px;height:68px;background:var(--purple-deep)}
.footer .copy{left:80px;top:24px;font-size:14px;color:var(--white)}
.footer .copy b{color:var(--green);font-weight:400}
.footer .icons{right:80px;top:12px;display:flex;gap:12px}
.footer .icons span{width:44px;height:44px;border-radius:50%;background:rgba(255,255,255,.25)}
</style>
</head>
<body>

<section class="section hero">
  <div class="abs hero-photo" role="img" aria-label="Photo of a diverse group of smiling students holding books and folders against a blue sky"></div>
  <h1 class="abs hero-title center">RESULTS THAT GO BEYOND<br>TRADITIONAL TUTORING</h1>
  <div class="abs slider-dots"><span></span><span></span><span></span></div>
</section>

<header class="section topbar">
  <div class="abs follow">FOLLOW US ON : <span class="dot-icon"></span><span class="dot-icon"></span><span class="dot-icon"></span><span class="dot-icon"></span></div>
  <div class="abs call">
    <svg width="14" height="20" viewBox="0 0 14 20"><rect x="1" y="1" width="12" height="18" rx="2" fill="none" stroke="#fff" stroke-width="2"/><circle cx="7" cy="15.5" r="1.3" fill="#fff"/></svg>
    CALL US ON : 555-014-2290
  </div>
</header>
<div class="brand"><span class="brand-mark"></span><span class="brand-name">HARBOR LIGHT<br>STUDY HOUSE</span></div>
<nav class="abs nav"><a href="#">HOME</a><a href="#">ABOUT</a><a href="#">SERVICES</a><a href="#">PORTFOLIO</a><a href="#">CONTACT</a></nav>

<section class="section programs">
  <svg class="abs" style="left:0;top:0" width="1200" height="552" viewBox="0 0 1200 552">
    <defs><marker id="arrow" viewBox="0 0 10 10" refX="8" refY="5" markerWidth="7" markerHeight="7" orient="auto"><path d="M0 0L10 5L0 10z" fill="#6b2a8c"/></marker></defs>
    <g stroke="#6b2a8c" stroke-width="3" fill="none" marker-end="url(#arrow)">
      <line x1="558" y1="97" x2="633" y2="97"/>
      <line x1="710" y1="120" x2="745" y2="175"/>
      <line x1="772" y1="252" x2="772" y2="295"/>
      <line x1="745" y1="363" x2="712" y2="418"/>
      <line x1="637" y1="455" x2="562" y2="455"/>
      <line x1="490" y1="432" x2="455" y2="377"/>
      <line x1="428" y1="300" x2="428" y2="257"/>
      <line x1="455" y1="189" x2="488" y2="134"/>
    </g>
    <g fill="#fff" stroke="#c7e39a" stroke-width="6">
      <circle cx="518" cy="97" r="40"/><circle cx="677" cy="97" r="40"/>
      <circle cx="428" cy="211" r="40"/><circle cx="772" cy="211" r="40"/>
      <circle cx="428" cy="340" r="40"/><circle cx="772" cy="340" r="40"/>
      <circle cx="518" cy="455" r="40"/><circle cx="677" cy="455" r="40"/>
    </g>
    <g fill="#6b2a8c">
      <circle cx="518" cy="97" r="14"/><circle cx="677" cy="97" r="14"/>
      <circle cx="428" cy="211" r="14"/><circle cx="772" cy="211" r="14"/>
      <circle cx="428" cy="340" r="14"/><circle cx="772" cy="340" r="14"/>
      <circle cx="518" cy="455" r="14"/><circle cx="677" cy="455" r="14"/>
    </g>
  </svg>
  <div class="abs hub" role="img" aria-label="Illustration of a purple brain held in green hands"></div>

  <div class="abs program" style="left:140px;top:57px"><h3>APEX</h3><p>(attention, memory, processing skills)<br>Strengthens specific processing deficits</p></div>
  <div class="abs program" style="left:64px;top:172px"><h3>Steady Steps Reading Program</h3><p>For students who have<br>decoding issues</p></div>
  <div class="abs program" style="left:64px;top:308px"><h3>Neurofeedback</h3><p>A.D.H.D, autism spectrum</p></div>
  <div class="abs program" style="left:152px;top:420px"><h3>On Beat</h3><p>instils timing and body awareness</p></div>

  <div class="abs program" style="left:748px;top:57px"><h3>Tuned Learning Ears</h3><p>For students who read for words and not<br>for meaning.</p></div>
  <div class="abs program" style="left:814px;top:172px"><h3>The Sound Path Program</h3><p>great for all aspects of learning</p></div>
  <div class="abs program" style="left:814px;top:308px"><h3>Picture &amp; Phrase</h3><p>For students who read well but<br>do not comprehend</p></div>
  <div class="abs program" style="left:741px;top:420px;width:360px"><h3>Number Bridges</h3><p>A Brightfield Program for grammar school<br>students struggling with basic math skills.</p></div>
</section>

<section class="section quote" role="img" aria-label="Purple-tinted photo of a student studying on a laptop">
  <div class="abs quote-mark center">&ldquo;</div>
  <p class="abs quote-text center">I try to have a solution for every parent who walks through our doors,<br>and I look forward to helping many more students in the future.</p>
  <p class="abs quote-by center">&mdash; Marion Ellery, Founder, Harbor Light Study House</p>
  <div class="abs socials"><span></span><span></span><span></span><span></span><span></span></div>
  <p class="abs socials-caption center">Find Us on Social Networks</p>
</section>

<section class="section why">
  <h2 class="abs">Why <b>CHOOSE</b> Us</h2>
  <p class="abs intro">Do you hear things like, "your child is lazy," or "he can't focus or attend."<br>If you answered yes to any of these questions, we can help</p>
  <ul class="abs checks">
    <li><svg width="18" height="18" viewBox="0 0 18 18"><circle cx="9" cy="9" r="9" fill="#8cc63f"/><path d="M5 9.5l3 3 5-6" stroke="#fff" stroke-width="2" fill="none"/></svg>Is school a struggle?</li>
    <li><svg width="18" height="18" viewBox="0 0 18 18"><circle cx="9" cy="9" r="9" fill="#8cc63f"/><path d="M5 9.5l3 3 5-6" stroke="#fff" stroke-width="2" fill="none"/></svg>Are you and your child spending twice as much time doing homework as you should be?</li>
    <li><svg width="18" height="18" viewBox="0 0 18 18"><circle cx="9" cy="9" r="9" fill="#8cc63f"/><path d="M5 9.5l3 3 5-6" stroke="#fff" stroke-width="2" fill="none"/></svg>Are you frustrated and at your wits end?</li>
    <li><svg width="18" height="18" viewBox="0 0 18 18"><circle cx="9" cy="9" r="9" fill="#8cc63f"/><path d="M5 9.5l3 3 5-6" stroke="#fff" stroke-width="2" fill="none"/></svg>Have you been told your child has a learning disability?</li>
  </ul>
  <div class="abs price"><strong>$50.00</strong><span>free consultation<br>for first time clients</span></div>
  <div class="abs why-photo" role="img" aria-label="Photo of a young girl sitting on a stack of books, holding a yellow book"></div>
</section>

<section class="section tutors" role="img" aria-label="Purple-tinted photo of city buildings">
  <h2 class="abs">Our <b>TUTORS</b></h2>
  <article class="abs card open" style="left:80px">
    <div class="photo" role="img" aria-label="Portrait photo of tutor Lena Marlowe"></div>
    <h3>LENA MARLOWE</h3>
    <p class="role">English Tutor</p>
    <p class="bio">Lorem Ipsum is simply dummy text of the printing</p>
    <div class="links"><span></span><span></span><span></span><span></span></div>
  </article>
  <article class="abs card" style="left:343px">
    <div class="photo" role="img" aria-label="Portrait photo of Owen Hartley"></div>
    <h3>OWEN HARTLEY</h3>
    <p class="role">Neurologist</p>
  </article>
  <article class="abs card" style="left:608px">
    <div class="photo" role="img" aria-label="Portrait photo of tutor Miles Carver"></div>
    <h3>MILES CARVER</h3>
    <p class="role">Math Tutor</p>
  </article>
  <article class="abs card" style="left:871px">
    <div class="photo" role="img" aria-label="Portrait photo of tutor Nora Whitfield"></div>
    <h3>NORA WHITFIELD</h3>
    <p class="role">Reading Tutor</p>
  </article>
</section>

<section class="section clients">
  <h2 class="abs">What <b>CLIENTS</b> say About Us</h2>
  <p class="abs intro">Lorem Ipsum is simply dummy text of the printing and typesetting industry. Lorem Ipsum has been the industry's standard dummy text ever since the 1500s.</p>

  <div class="abs avatar" style="left:195px" role="img" aria-label="Portrait photo of client Tobin Reyes"></div>
  <div class="abs avatar" style="left:552px" role="img" aria-label="Portrait photo of client Ada Kimber"></div>
  <div class="abs avatar" style="left:906px" role="img" aria-label="Portrait photo of client Felix Ardent"></div>

  <p class="abs client-name" style="left:78px">Tobin Reyes</p>
  <p class="abs client-name" style="left:435px">Ada Kimber</p>
  <p class="abs client-name" style="left:789px">Felix Ardent</p>

  <blockquote class="abs review" style="left:78px">" Lorem Ipsum is simply dummy text of the printing and typesetting industry. Lorem Ipsum has been the industry's standard dummy text ever since the 1500s"</blockquote>
  <blockquote class="abs review" style="left:434px">" Lorem Ipsum is simply dummy text of the printing and typesetting industry. Lorem Ipsum has been the industry's standard dummy text ever since the 1500s"</blockquote>
  <blockquote class="abs review" style="left:792px">" Lorem Ipsum is simply dummy text of the printing and typesetting industry. Lorem Ipsum has been the industry's standard dummy text ever since the 1500s"</blockquote>
</section>

<section class="section contact" role="img" aria-label="Purple-tinted photo of a smiling family">
  <h2 class="abs">Happy to Hear from <b>YOU</b></h2>
  <p class="abs label" style="left:78px;top:136px">INQUIRY FORM</p>
  <div class="abs field" style="left:78px;top:170px;width:219px">Name</div>
  <div class="abs field" style="left:316px;top:170px;width:219px">E-Mail</div>
  <div class="abs field" style="left:555px;top:170px;width:219px">Subject</div>
  <div class="abs field" style="left:78px;top:231px;width:696px;height:146px">Message</div>
  <div class="abs send">
    <svg width="30" height="22" viewBox="0 0 30 22"><rect x="1" y="1" width="28" height="20" rx="2" fill="#fff"/><path d="M2 2l13 10 13-10" stroke="#6b2a8c" stroke-width="2" fill="none"/></svg>
  </div>

  <p class="abs label info" style="top:136px">CONTACT INFO</p>
  <svg class="abs" style="left:971px;top:172px" width="34" height="42" viewBox="0 0 34 42"><path d="M17 40C17 40 3 24 3 15a14 14 0 0 1 28 0c0 9-14 25-14 25z" fill="none" stroke="#fff" stroke-width="2.5"/><circle cx="17" cy="15" r="5" fill="none" stroke="#fff" stroke-width="2.5"/></svg>
  <p class="abs info" style="top:222px">418 Lantern Row, Bayview, ST 00100</p>
  <svg class="abs" style="left:972px;top:256px" width="32" height="32" viewBox="0 0 32 32"><path d="M8 3l5 7-3 3c2 4 5 7 9 9l3-3 7 5-3 5C16 29 3 16 3 6z" fill="none" stroke="#fff" stroke-width="2.5" stroke-linejoin="round"/></svg>
  <p class="abs info" style="top:298px">555-014-2290</p>
  <svg class="abs" style="left:972px;top:330px" width="32" height="24" viewBox="0 0 32 24"><rect x="1.5" y="1.5" width="29" height="21" fill="none" stroke="#fff" stroke-width="2.5"/><path d="M2 2l14 11 14-11" fill="none" stroke="#fff" stroke-width="2.5"/></svg>
  <p class="abs info" style="top:358px;left:858px;width:260px">info@harborlightstudyhouse.example</p>
</section>

<footer class="section footer">
  <p class="abs copy">&copy; <b>HARBOR LIGHT STUDY HOUSE</b> - 2016. All Rights Reserved</p>
  <div class="abs icons"><span></span><span></span><span></span><span></span></div>
</footer>

</body>
</html>
```